Label for Gin Bottle - Cranberry & Peach

Hi, We have created a Cranberry & Peach Gin that we require a label for.
The gin will be a vivid Orange/red colour in a clear 50cl bottle
The gin will be 40% Vol.
I am looking for a classy design with a summer/fresh appearance.
Thank You.

```html
<!DOCTYPE html>
<html lang="en">
<head>
<meta charset="utf-8">
<title>Gin Labels – Cranberry & Peach</title>
<link href="https://fonts.googleapis.com/css2?family=Pinyon+Script&family=Montserrat:wght@500&display=swap" rel="stylesheet">
<style>
  :root {
    --page: #efefef;
    --band: #0b0b0b;
    --band-rule: #9a9a9a;
    --ink-light: #e4e4e4;
    --badge: #151515;
    --badge-ring: #bcbcbc;
    --cranberry-deep: #4a060d;
    --cranberry-mid: #9c1020;
    --cranberry-bright: #e0324a;
    --peach-deep: #e4761a;
    --peach-mid: #f7a445;
    --peach-light: #ffd08f;
  }
  * { margin: 0; padding: 0; box-sizing: border-box; }
  html, body {
    width: 1200px; height: 1000px; overflow: hidden;
    background: var(--page);
  }
  .canvas {
    position: relative; width: 1200px; height: 1000px;
    background: radial-gradient(ellipse at center, #ffffff 0%, var(--page) 75%);
  }
  .label {
    position: absolute; top: 290px; width: 470px; height: 520px;
  }
  .label--cranberry { left: 95px; }
  .label--peach { left: 635px; }
  .label__badge {
    position: absolute; left: 50%; top: 0; transform: translateX(-50%);
    width: 164px; height: 164px; border-radius: 50%;
    background: var(--badge);
    border: 2px solid var(--badge-ring);
    box-shadow: inset 0 0 0 7px var(--badge), inset 0 0 0 8px var(--badge-ring);
    display: flex; align-items: center; justify-content: center;
    z-index: 2;
  }
  .label__brand {
    font-family: "Montserrat", sans-serif; font-weight: 500;
    font-size: 16px; letter-spacing: 3px; text-transform: uppercase;
    color: var(--badge-ring);
  }
  .label__fruit {
    position: absolute; top: 100px; left: 0; width: 100%; height: 300px;
    border-top: 2px solid var(--band);
  }
  .label--cranberry .label__fruit {
    background:
      linear-gradient(180deg, rgba(0,0,0,0) 55%, rgba(40,0,6,0.45) 100%),
      radial-gradient(ellipse at 60% 35%, var(--cranberry-bright) 0%, var(--cranberry-mid) 40%, var(--cranberry-deep) 100%);
  }
  .label--peach .label__fruit {
    background:
      linear-gradient(180deg, rgba(0,0,0,0) 60%, rgba(150,60,0,0.3) 100%),
      radial-gradient(ellipse at 45% 40%, var(--peach-light) 0%, var(--peach-mid) 45%, var(--peach-deep) 100%);
  }
  .label__band {
    position: absolute; top: 400px; left: 0; width: 100%; height: 120px;
    background: var(--band);
    border-top: 2px solid var(--band-rule);
    border-bottom: 2px solid var(--band-rule);
    display: flex; flex-direction: column; align-items: center; justify-content: center;
  }
  .label__name {
    font-family: "Pinyon Script", cursive; font-weight: 400;
    font-size: 46px; color: var(--ink-light); line-height: 1.1;
  }
  .label__abv {
    margin-top: 8px;
    font-family: "Montserrat", sans-serif; font-weight: 500;
    font-size: 11px; letter-spacing: 1px; color: var(--ink-light);
  }
</style>
</head>
<body>
<main class="canvas">
  <section class="label label--cranberry">
    <div class="label__badge"><span class="label__brand">Ashgrove</span></div>
    <div class="label__fruit" role="img" aria-label="Photograph of glossy fresh red cranberries filling the frame"></div>
    <div class="label__band">
      <h1 class="label__name">Cranberry Gin</h1>
      <p class="label__abv">40% VOL.</p>
    </div>
  </section>
  <section class="label label--peach">
    <div class="label__badge"><span class="label__brand">Ashgrove</span></div>
    <div class="label__fruit" role="img" aria-label="Photograph of ripe orange peaches piled together filling the frame"></div>
    <div class="label__band">
      <h1 class="label__name">Peach Gin</h1>
      <p class="label__abv">40% VOL.</p>
    </div>
  </section>
</main>
</body>
</html>
```